Fairway Relief Rockets promotional cards (rack card)

This will be an eye catching (rack) card designed to be left at the Golf clubhouse with special event coordinators and emailed or physically handed to charities conducting fund raising golf tournaments. I need an electronic file version that I could email to prospects to view before they decide if they will help promote this to their tournament directors
Photos, logos, files and website link are attached. all photos on my website are available upon request.
www.fairwayreliefrockets.com
Target Market(s)
must be appealing to charities conducting golf tournaments as a method to raise funds,
Industry/Entity Type
Golf Course
Font styles to use
Other font styles liked:
- Screwed Oblique for any bold type, serif for body text
Requirements
Must have
- include a call to action to "book your event now"
- use the colors in my logo
- include the photo attached, could include additional photos from my website
- include "several packages to choose from"
- I would like this to be vectorized to be able to resize or shrink slightly as needed to fit printables.
Nice to have
- in the background of photos, there is a 7 foot pull up banner that participants often stand in front of to take videos and photos, you can incorporate that if possible as a watermark or background image. I can provide that original image if needed.
Should not have
- any salesy "car commercial" banners or balloons or stars or anything like that.

```html
<!DOCTYPE html>
<html lang="en">
<head>
<meta charset="utf-8">
<title>Fairway Relief Rockets – Rack Card</title>
<link href="https://fonts.googleapis.com/css2?family=Russo+One&family=Oswald:wght@400;500&family=Lato:wght@400;700&display=swap" rel="stylesheet">
<style>
  :root{
    --backdrop:#a9b6c2;
    --mint:#9fcf9f;
    --mint-soft:#a8d4a6;
    --forest:#1d5c30;
    --forest-deep:#144524;
    --leaf:#58b455;
    --ink:#0f2a17;
    --white:#ffffff;
  }
  *{margin:0;padding:0;box-sizing:border-box}
  html,body{width:1200px;height:1105px;overflow:hidden;background:var(--backdrop)}
  body{position:relative;font-family:"Lato",sans-serif;color:var(--white)}

  .card{position:absolute;top:46px;height:1022px;background:var(--mint);box-shadow:0 3px 10px rgba(0,0,0,.25)}
  .card--front{left:62px;width:456px}
  .card--back{left:698px;width:454px}

  /* front */
  .brand-stack{position:absolute;left:0;top:0;width:456px;height:299px;font-family:"Russo One",sans-serif;color:var(--forest);text-transform:uppercase}
  .brand-stack span{position:absolute;font-size:56px;line-height:1;letter-spacing:1px}
  .brand-stack .l1{left:52px;top:40px}
  .brand-stack .l2{left:122px;top:112px}
  .brand-stack .l3{left:160px;top:184px}

  .hero-photo{position:absolute;left:0;top:299px;width:456px;height:345px;
    background:linear-gradient(180deg,#3d5a35 0%,#5d7f48 40%,#6f9a52 70%,#4f7a3a 100%)}
  .hero-invite{position:absolute;right:0;top:120px;width:204px;height:130px;background:rgba(40,50,45,.6);
    font-family:"Oswald",sans-serif;font-size:19px;line-height:40px;text-align:right;padding:10px 18px 0 0;letter-spacing:.5px;text-transform:uppercase}
  .packages-tab{position:absolute;left:60px;top:612px;width:396px;height:40px;background:var(--white);
    border-radius:20px 0 0 0;font-family:"Oswald",sans-serif;font-weight:500;font-size:19px;color:var(--ink);
    display:flex;align-items:center;justify-content:center;letter-spacing:.3px}

  .front-body{position:absolute;left:0;top:644px;width:456px;height:378px;background:var(--forest);padding:18px 22px 0 24px;font-size:10.8px;line-height:14.5px}
  .front-body p{margin-bottom:14px}
  .front-body .opt{margin-bottom:6px}
  .opt b{color:var(--leaf);font-weight:400}
  .cta{font-family:"Russo One",sans-serif;font-size:21px;text-transform:uppercase;transform:skewX(-12deg);margin-top:14px;padding-left:12px;letter-spacing:.5px}
  .cta-phone{font-family:"Russo One",sans-serif;font-size:21px;color:var(--ink);transform:skewX(-12deg);padding-left:84px;margin-top:10px;letter-spacing:1px}

  /* back */
  .back-header{position:absolute;left:10px;top:14px;width:434px;height:78px;background:var(--forest);
    font-family:"Russo One",sans-serif;font-size:25px;color:var(--mint);display:flex;align-items:center;justify-content:center;text-transform:uppercase;letter-spacing:.5px}
  .back-top{position:absolute;left:10px;top:100px;width:434px;height:450px;background:var(--forest)}
  .photo{position:absolute;left:0;width:164px}
  .photo--shooters{top:0;height:145px;background:linear-gradient(160deg,#3f5e3a,#7d8f6a 55%,#3a4d33)}
  .photo--target{top:153px;height:142px;background:linear-gradient(180deg,#8fb2cc 0%,#b7cad6 30%,#5d7e40 48%,#77a34c 100%)}
  .photo--team{top:303px;height:147px;background:linear-gradient(180deg,#4d6b3c,#7ea35b 55%,#5e8647)}
  .back-intro{position:absolute;left:174px;top:6px;width:254px;font-size:10.6px;line-height:13.4px;text-align:justify}
  .back-intro p{margin-bottom:13px}

  .back-bottom{position:absolute;left:10px;top:558px;width:434px;height:452px;background:var(--forest);padding:14px 12px 0 12px;font-size:10.6px;line-height:13.6px}
  .back-bottom p{margin-bottom:13px}
  .back-bottom .label{color:var(--leaf);font-weight:700}
  .booking{text-align:center;font-weight:700;margin-top:4px}
  .follow{font-family:"Russo One",sans-serif;font-size:14px;color:var(--ink);text-align:center;transform:skewX(-12deg);margin-top:12px;letter-spacing:1px}
  .social{display:flex;justify-content:center;gap:12px;margin-top:10px}
  .social span{width:22px;height:22px;border-radius:50%;background:var(--mint-soft)}
  .hashtag{font-family:"Russo One",sans-serif;font-size:14px;color:var(--ink);text-align:center;transform:skewX(-12deg);margin-top:12px;letter-spacing:.5px}
  .contact-row{display:flex;justify-content:space-between;font-weight:700;font-size:10.5px;margin-top:16px}
</style>
</head>
<body>

<section class="card card--front">
  <div class="brand-stack" aria-label="Fairway Relief Rockets">
    <span class="l1">Fairway</span>
    <span class="l2">Relief</span>
    <span class="l3">Rockets</span>
  </div>

  <div class="hero-photo" role="img" aria-label="Photo of a participant firing the golf ball launcher on a course, with the pull-up event banner behind">
    <div class="hero-invite">Come,<br>Join us for this<br>Thrilling adventure</div>
  </div>
  <div class="packages-tab">SEVERAL PACKAGES TO CHOOSE FROM</div>

  <div class="front-body">
    <p>We have several package options to choose from that are guaranteed to make your next golf event a memorable one!</p>
    <p>Your players will be talking about this one all day long! It is completely safe, fun and an experience that all ages can participate in.</p>
    <p class="opt" style="font-weight:700">Packages available:</p>
    <p class="opt"><b>Option 1:</b> ($250 fee) $5 or $10 per player/per shot (player pays to participate) ( player provides a ball)</p>
    <p class="opt"><b>Option 2:</b> ($500 fee -sponsor level) $5 or $10 per player/per shot and I provide all players a logo ball) 100% profit to the charity</p>
    <p class="opt"><b>Option 3:</b> ($500 fee -sponsor level) player participation is included in mulligan package price. 100% profit to the charity</p>
    <p class="opt"><b>Option 4:</b> Custom package design based upon charity requests</p>
    <div class="cta">Book your tournament!</div>
    <div class="cta-phone">555-014-2278</div>
  </div>
</section>

<section class="card card--back">
  <div class="back-header">Fairway Relief Rockets</div>

  <div class="back-top">
    <div class="photo photo--shooters" role="img" aria-label="Photo of two participants with ear protection holding the launcher"></div>
    <div class="photo photo--target" role="img" aria-label="Photo of a target set on a fairway"></div>
    <div class="photo photo--team" role="img" aria-label="Photo of players at the launch tee beside a canopy"></div>
    <div class="back-intro">
      <p>I have been referred to you by a previous supporter/participant in one of your past charity events.</p>
      <p>I would like to introduce Fairway Relief Rockets: Are you tired or bored of the same old challenges at every charity golf tournament? How about adding an alternative to your typical golf tournament fundraising efforts. I provide an excitement by providing an RX-9 golf ball launcher.</p>
      <p>Mulligans, longest drive, putting contests, Hole in One for a car? Yeah, you've been there and done that!</p>
      <p>Now it is time to add a new challenge? How about a prize for closest to the 400 yard target? Set up: Preferably a par 4 or par 5 hole with a straight line of sight out to around 400-yards and away from any obstacles if possible.</p>
      <p>I give your registered players making a donation, the opportunity to use the rifle to launch their golf ball approximately 375-400 yards in place of driving off a tee.</p>
    </div>
  </div>

  <div class="back-bottom">
    <p><span class="label">Approval:</span> I request that the tournament director and the golf course clubhouse manager both acknowledge that they have approved of the use of the RX-9 golf ball launcher and are aware of the noise associated with it, and assume all liabilities beyond the teebox as they do for any other promotional event occurring on their course.</p>
    <p>(Ie- longest drive, hole in one, involving a participant teeing off.)</p>
    <p><span class="label">Collecting funds:</span> I provide two options for collecting funds. The preferred method is to have players make a donation at the selected hole. The alternative is to accept credit cards via card register at the hole for players who do not have cash but would like to make a donation anyways.</p>
    <p>Cash, tickets and card register totals are turned in after the final foursome fires away! I would love to help you raise funds while providing an exciting new option for your players!</p>
    <p class="booking">To book your date, please feel free to email me or call me.</p>
    <div class="follow">FOLLOW US ON</div>
    <div class="social" aria-label="Social channels"><span></span><span></span><span></span><span></span><span></span><span></span></div>
    <div class="hashtag">#FAIRWAYRELIEFROCKETS</div>
    <div class="contact-row">
      <span>Dana@fairwayreliefrockets.com</span>
      <span>555-014-2278</span>
      <span>www.fairwayreliefrockets.com</span>
    </div>
  </div>
</section>

</body>
</html>
```